IT Company requires new Business Card design.

Over the years we have had a few different business card designs. We are now due for new cards across the board for all staff. We felt this would be a good time to start fresh with a new design. Our traditional card simply had our details on the front, and a list of services on the back. We don't particularly need the list of services, we have had cards where the only thing on the rear of the card was our logo.
Feel free to be creative, we would like our tag line "Complete IT Management" to appear at some point, doesn't necessarily have to be with the logo.
I have attached samples and drafts of various previous cards we have used over the years.

```html
<!DOCTYPE html>
<html lang="en">
<head>
<meta charset="utf-8">
<title>Brook Networking – Business Card</title>
<link rel="stylesheet" href="https://fonts.googleapis.com/css2?family=Arimo:wght@400;700&display=swap">
<style>
  :root {
    --page: #ffffff;
    --card: #3a3a3a;
    --accent: #29a8e0;
    --ink: #ffffff;
    --mark: #1c93cf;
  }
  * { box-sizing: border-box; margin: 0; padding: 0; }
  html, body {
    width: 1200px;
    height: 350px;
    overflow: hidden;
    background: var(--page);
    font-family: "Arimo", Arial, sans-serif;
    color: var(--ink);
  }
  .sheet { position: relative; width: 1200px; height: 350px; }
  .card {
    position: absolute;
    top: 0;
    height: 350px;
    background: var(--card);
  }
  .card--front { left: 0; width: 595px; }
  .card--back { left: 605px; width: 595px; }

  /* front */
  .brand-square {
    position: absolute;
    left: 92px;
    top: 110px;
    width: 110px;
    height: 110px;
    background: var(--mark);
  }
  .brand-name {
    position: absolute;
    left: 262px;
    top: 92px;
    font-weight: 700;
    color: var(--ink);
    line-height: 1;
  }
  .brand-name__first { display: block; font-size: 72px; letter-spacing: 1px; }
  .brand-name__second { display: block; font-size: 39px; margin-top: 4px; letter-spacing: 0.5px; }
  .tagline {
    position: absolute;
    left: 260px;
    top: 206px;
    font-size: 15px;
    letter-spacing: 3.2px;
    color: var(--accent);
  }

  /* back */
  .back-brand {
    position: absolute;
    right: 60px;
    top: 56px;
    font-size: 16px;
    font-weight: 700;
    letter-spacing: 1px;
    color: var(--ink);
  }
  .person {
    position: absolute;
    right: 22px;
    top: 106px;
    text-align: right;
  }
  .person__name {
    font-size: 45px;
    font-weight: 400;
    line-height: 1;
    color: var(--ink);
  }
  .person__role {
    margin-top: 8px;
    margin-right: 10px;
    font-size: 17px;
    letter-spacing: 0.5px;
    color: var(--accent);
  }
  .contact {
    position: absolute;
    right: 20px;
    top: 219px;
    text-align: right;
    font-size: 14px;
    font-weight: 700;
    line-height: 21px;
  }
  .contact__label { color: var(--accent); margin-right: 4px; }
  .contact__email { color: var(--accent); font-size: 15px; }
  .contact__email span { color: var(--ink); }
  .address {
    position: absolute;
    left: 170px;
    top: 286px;
    font-size: 13.5px;
    font-weight: 700;
    line-height: 20px;
  }
  .address__po { letter-spacing: 3.1px; }
</style>
</head>
<body>
<main class="sheet">
  <section class="card card--front">
    <div class="brand-square"></div>
    <h1 class="brand-name">
      <span class="brand-name__first">BROOK</span>
      <span class="brand-name__second">NETWORKING</span>
    </h1>
    <p class="tagline">COMPLETE IT MANAGEMENT</p>
  </section>

  <section class="card card--back">
    <p class="back-brand">BROOK</p>
    <div class="person">
      <h2 class="person__name">Daniel Okafor</h2>
      <p class="person__role">WEB PROJECT MANAGER</p>
    </div>
    <div class="contact">
      <p><span class="contact__label">P:</span>(08) 5550 1230 | &nbsp;&nbsp;&nbsp;&nbsp;(08) 5550 1232</p>
      <p><span class="contact__label">W:</span>&nbsp;&nbsp;www.brooknetworking.example</p>
      <p class="contact__email">dan<span>@brooknetworking.example</span></p>
    </div>
    <div class="address">
      <p><span class="contact__label">A:</span>Unit 4, 12 Marlow Street, Harbourview WA 6100</p>
      <p class="address__po">PO Box 1287, Fairfield WA 6900</p>
    </div>
  </section>
</main>
</body>
</html>
```